Updated Business Card Design more modern and eye catching

looking for something more dynamic than the sterile card we have now. Please take a look at our web site www.brindlemarket.net to see what we do. only looking for the front side of the card for now. I've also attached a sample of a card with raised spot uv ink - it might be cool to incorporate something like that. Card should be bold yet serious. No frilly or scrolly stuff on it.
Updates
Target Market(s)
We do decor and signage for retail business and supermarkets. Our new name should reflect that we're hip but serious.
Contact Information for Business Card
standard business card size - horizontal preferred
Font styles to use
Requirements
Must have
- Current logo and colors cannot be changed.
Nice to have
- Must have information shown on existing card but open to some changes. Okay to consider spot uv.
Should not have
- Not busy with pictures in the background.

```html
<!DOCTYPE html>
<html lang="en">
<head>
<meta charset="utf-8">
<title>Brindle Market – Business Card</title>
<link rel="stylesheet" href="https://fonts.googleapis.com/css2?family=Michroma&family=Open+Sans:wght@400;600&display=swap">
<style>
  :root {
    --backdrop: #8c5024;
    --gold: #b5a752;
    --ink: #111111;
    --paper: #ffffff;
    --brand-ink: #1d1d1d;
  }
  html, body {
    margin: 0;
    padding: 0;
    width: 1200px;
    height: 900px;
    overflow: hidden;
    background: var(--backdrop);
  }
  .stage {
    position: relative;
    width: 1200px;
    height: 900px;
  }
  .card {
    position: absolute;
    box-shadow: 3px 4px 6px rgba(0,0,0,0.45);
  }
  .card-front {
    left: 330px;
    top: 90px;
    width: 555px;
    height: 343px;
    background: var(--gold);
    color: var(--ink);
    font-family: "Open Sans", Arial, sans-serif;
    text-align: center;
  }
  .card-back {
    left: 330px;
    top: 469px;
    width: 559px;
    height: 343px;
    background: var(--paper);
  }
  .person-name {
    position: absolute;
    left: 0; right: 0;
    top: 60px;
    margin: 0;
    font-family: "Michroma", "Open Sans", sans-serif;
    font-size: 17px;
    font-weight: 400;
    letter-spacing: 2.5px;
    line-height: 24px;
  }
  .person-title {
    position: absolute;
    left: 0; right: 0;
    top: 82px;
    margin: 0;
    font-size: 15px;
    line-height: 20px;
  }
  .icon-row {
    position: absolute;
    left: 181px;
    top: 113px;
  }
  .contact-list {
    position: absolute;
    left: 0; right: 0;
    top: 140px;
    margin: 0;
    padding: 0;
    list-style: none;
    font-size: 15.5px;
    line-height: 20px;
  }
  .rule {
    position: absolute;
    left: 181px;
    top: 231px;
    width: 193px;
    height: 1px;
    background: var(--ink);
  }
  .address {
    position: absolute;
    left: 0; right: 0;
    top: 240px;
    margin: 0;
    font-style: normal;
    font-size: 15.5px;
    line-height: 20px;
  }
  .brand {
    position: absolute;
    left: 0; right: 0;
    top: 150px;
    display: flex;
    align-items: center;
    justify-content: center;
    gap: 14px;
  }
  .brand-mark {
    width: 30px;
    height: 30px;
    background: var(--gold);
  }
  .brand-name {
    font-family: "Open Sans", Arial, sans-serif;
    font-weight: 600;
    font-size: 30px;
    letter-spacing: 2px;
    color: var(--brand-ink);
  }
</style>
</head>
<body>
<main class="stage">
  <section class="card card-front" aria-label="Card front">
    <h1 class="person-name">MARA LINDEN</h1>
    <p class="person-title">Vice-President</p>

    <svg class="icon-row" width="193" height="20" viewBox="0 0 193 20" aria-hidden="true">
      <line x1="0" y1="10" x2="42" y2="10" stroke="#111" stroke-width="1"/>
      <line x1="151" y1="10" x2="193" y2="10" stroke="#111" stroke-width="1"/>
      <!-- phone -->
      <rect x="46" y="0" width="20" height="20" fill="#111"/>
      <path d="M50 9 q6 -5 12 0 v2 h-3 v-2 h-6 v2 h-3z M51 12 h10 v4 h-10z" fill="#b5a752"/>
      <!-- mobile -->
      <rect x="71" y="0" width="20" height="20" fill="#111"/>
      <rect x="76.5" y="3.5" width="9" height="13" rx="1" fill="none" stroke="#b5a752" stroke-width="1.4"/>
      <!-- mail -->
      <rect x="96" y="0" width="20" height="20" fill="#111"/>
      <rect x="99.5" y="5" width="13" height="10" fill="none" stroke="#b5a752" stroke-width="1.4"/>
      <path d="M99.5 5 l6.5 5.5 l6.5 -5.5" fill="none" stroke="#b5a752" stroke-width="1.4"/>
      <!-- globe -->
      <rect x="121" y="0" width="20" height="20" fill="#111"/>
      <circle cx="131" cy="10" r="6" fill="#b5a752"/>
      <path d="M128 7 q2 1 2 3 q2 1 1 4 M133 5 q1 2 2 2" fill="none" stroke="#111" stroke-width="1"/>
    </svg>

    <ul class="contact-list">
      <li>555.210.4817</li>
      <li>555.368.9052 ext.3</li>
      <li>Mara@BrindleMarket.net</li>
      <li>www.brindlemarket.net</li>
    </ul>
    <div class="rule"></div>
    <address class="address">4120 Commerce Way<br>Harbor Point, FL 30418</address>
  </section>

  <section class="card card-back" aria-label="Card back">
    <div class="brand">
      <span class="brand-mark"></span>
      <span class="brand-name">BRINDLE MARKET</span>
    </div>
  </section>
</main>
</body>
</html>
```